Bref créative
Harbor Building Partners Company Brochure
HBP Brochure
"We Strive to Exceed Our Customers Expectations"
We're looking for a simple, yet unique and eye catching brochure in a unique format (8 1/2" by 8 1/2"). Each side should be 8 ½" x 8 ½" so that when it is open it is 8 ½" x 17"...or other dimensions that are unique and can easily fit in a portfolio case that's normally 9" x 12" maximum). Should have front cover, inside of front cover, inside of back cover, and back cover...a 4-part brochure. Vibrant and colorful, yet attempting to use the colors of our logo (which was designed by MarkCraftStudio more than a year ago)...colors are vibrant red, grey, and black. Want to include a listing of our services, our mission statement, what sets us apart, and contact info. We're thinking that the text should be superimposed over construction photos. So that each of the inside pages are a large, full page photo and the text strategically positioned on each page. Not sure how the front cover should look...but it could quite simply just have our company logo (which includes our name). The back cover could be red...with just simply our website address.
All of these are just selections as I'm no designer...but I want this brochure to convey that Harbor Building is a "solid company", and want those who view this brochure to get feelings that Harbor Building is secure, stable, capable...yet different as we're a newly formed (less than 2 years old) company that goes all out with customer service and commitment to perform above the clients expectations.
We have all the verbiage/text written...but will need it strategically placed and formatted.
Construction
Architects, Owners of Commercial Properties, Real Estate Investment Trusts, Universities, Hospitals, Non-Profit Organizations, Local and Federal Government Agencies…want our card to convey stability, professionalism, high-energy, performance driven…and want the card to catch their eye. Our target of Architects like “flash”…our Investment Trusts, Government entities like strong, confident, stable, no-risk, proven performer.
Don't think I can say more than what I've said. Like I've said before, we're the new firm in a town (Washington, DC) that has a lot of well established construction general contractors. We need something that will catch someone's eye, yet not be frilly or silly, to the point they'll want to read more inside.
Here's our current logo that we love, which was created by MarkCraftStudio

```html
<!DOCTYPE html>
<html lang="en">
<head>
<meta charset="utf-8">
<title>Harbor Building Partners Brochure</title>
<link href="https://fonts.googleapis.com/css2?family=Oswald:wght@500;700&family=Open+Sans:wght@400;600;700&display=swap" rel="stylesheet">
<style>
  :root {
    --red: #c4161c;
    --red-dark: #8e0f13;
    --grey: #8a8d91;
    --grey-light: #e6e6e6;
    --black: #111111;
    --white: #ffffff;
    --stage: #efece9;
  }
  * { box-sizing: border-box; margin: 0; padding: 0; }
  html, body { width: 1200px; height: 909px; overflow: hidden; }
  body { background: var(--stage); font-family: "Open Sans", sans-serif; position: relative; }

  .spread { position: absolute; left: 180px; width: 840px; height: 410px; display: flex; box-shadow: 0 6px 18px rgba(0,0,0,.18); }
  .spread--outside { top: 36px; }
  .spread--inside { top: 466px; }
  .page { position: relative; width: 420px; height: 410px; overflow: hidden; }

  /* back cover */
  .back-cover { background: linear-gradient(160deg, var(--red) 0%, var(--red-dark) 100%); }
  .back-cover .brand { position: absolute; left: 50%; top: 50%; transform: translate(-50%, -50%); color: var(--white); }

  /* brand lockup */
  .brand { display: flex; align-items: center; gap: 8px; font-family: "Oswald", sans-serif; font-weight: 700; font-size: 24px; line-height: 1; white-space: nowrap; }
  .brand__mark { width: 14px; height: 14px; background: currentColor; }
  .brand--red { color: var(--red); }

  /* front cover */
  .front-cover { background: var(--white); }
  .front-cover .brand { position: absolute; left: 26px; top: 34px; font-size: 30px; }
  .front-cover__photo { position: absolute; inset: 0; background: linear-gradient(150deg, #6b8fb8 0%, #9eb6cf 40%, #d9a23a 70%, #2d3a4a 100%); clip-path: polygon(100% 20%, 100% 100%, 52% 100%); }
  .front-cover__band { position: absolute; inset: 0; background: var(--red); clip-path: polygon(0 34%, 80% 34%, 42% 100%, 0 100%); }
  .front-cover__grey { position: absolute; inset: 0; background: var(--grey-light); clip-path: polygon(80% 34%, 86% 34%, 48% 100%, 42% 100%); }
  .front-cover__tagline { position: absolute; left: 22px; top: 164px; width: 230px; color: var(--white); font-family: "Oswald", sans-serif; text-transform: uppercase; line-height: 1.05; }
  .front-cover__tagline small { display: block; font-size: 13px; font-weight: 500; letter-spacing: 1px; margin-bottom: 4px; }
  .front-cover__tagline strong { display: block; font-size: 30px; font-weight: 700; }

  /* inside left */
  .inside-left { background: var(--white); }
  .inside-left__site { position: absolute; left: 0; top: 0; width: 100%; height: 170px; background: linear-gradient(180deg, #6a4c86 0%, #b8687e 60%, #e0a07a 100%); }
  .inside-left__helmet { position: absolute; left: 0; top: 170px; width: 100%; height: 110px; background: linear-gradient(135deg, #f3c21b 0%, #d99a10 45%, #cfd3d6 100%); }
  .mission { position: absolute; left: 0; bottom: 0; width: 100%; height: 130px; background: var(--white); padding: 16px 22px; }
  .heading { font-family: "Oswald", sans-serif; font-weight: 700; font-size: 15px; text-transform: uppercase; display: flex; align-items: center; gap: 6px; margin-bottom: 8px; }
  .heading::before { content: ""; width: 8px; height: 8px; background: var(--red); }
  .mission .heading { color: var(--black); }
  .body-text { font-size: 10px; line-height: 1.55; }
  .mission .body-text { color: #444; width: 300px; }

  /* inside right */
  .inside-right { background: var(--black); color: #cfcfcf; }
  .inside-right__skyline { position: absolute; left: 0; top: 0; width: 100%; height: 120px; background: linear-gradient(180deg, #5c4a7a 0%, #b46a7e 70%, #111 100%); }
  .info-columns { position: absolute; left: 22px; right: 22px; top: 140px; display: flex; gap: 20px; }
  .info-columns .col { flex: 1; }
  .info-columns .heading { color: var(--white); }
  .thumb { width: 70px; height: 48px; margin-bottom: 10px; }
  .thumb--one { background: linear-gradient(135deg, #9a8a6a, #4a4a4a); }
  .thumb--two { background: linear-gradient(135deg, #b9a58a, #3d3d3d); }
  .services { position: absolute; left: 22px; right: 22px; bottom: 14px; border-top: 2px solid var(--red); padding-top: 10px; }
  .services .heading { color: var(--white); }
  .services ul { list-style: none; display: flex; flex-wrap: wrap; gap: 4px 20px; font-size: 10px; font-weight: 600; }
  .services li { display: flex; align-items: center; gap: 5px; white-space: nowrap; }
  .services svg { flex: none; }
</style>
</head>
<body>

<section class="spread spread--outside">
  <div class="page back-cover">
    <div class="brand"><span class="brand__mark"></span>Harbor Building</div>
  </div>
  <div class="page front-cover">
    <div class="front-cover__photo" role="img" aria-label="Construction workers in hard hats reviewing plans in front of a city skyline"></div>
    <div class="front-cover__grey"></div>
    <div class="front-cover__band"></div>
    <div class="brand brand--red"><span class="brand__mark"></span>Harbor Building</div>
    <p class="front-cover__tagline"><small>We strive to</small><strong>Exceed</strong><strong>Expectations</strong></p>
  </div>
</section>

<section class="spread spread--inside">
  <div class="page inside-left">
    <div class="inside-left__site" role="img" aria-label="Steel building frame under construction at sunset"></div>
    <div class="inside-left__helmet" role="img" aria-label="Yellow hard hat resting on construction blueprints"></div>
    <div class="mission">
      <h2 class="heading">Mission</h2>
      <p class="body-text">Harbor Building Partners delivers every project on time and on budget, with a team that treats each client like our only client.</p>
    </div>
  </div>
  <div class="page inside-right">
    <div class="inside-right__skyline" role="img" aria-label="Construction cranes over a skyline at dusk"></div>
    <div class="info-columns">
      <div class="col">
        <h2 class="heading">Why Choose Us</h2>
        <p class="body-text">Clear schedules, honest pricing and daily site reports keep owners informed from groundbreaking to final walkthrough.</p>
      </div>
      <div class="col">
        <div class="thumb thumb--one" role="img" aria-label="Finished commercial interior"></div>
        <div class="thumb thumb--two" role="img" aria-label="Completed office lobby"></div>
        <p class="body-text">Our crews bring safety, precision and pride to commercial, healthcare, education and government work across the region.</p>
      </div>
    </div>
    <div class="services">
      <h2 class="heading">Services</h2>
      <ul>
        <li><svg width="8" height="8" viewBox="0 0 8 8"><path d="M1 4l2 2 4-5" stroke="#c4161c" stroke-width="1.5" fill="none"/></svg>General Contracting</li>
        <li><svg width="8" height="8" viewBox="0 0 8 8"><path d="M1 4l2 2 4-5" stroke="#c4161c" stroke-width="1.5" fill="none"/></svg>Construction Management</li>
        <li><svg width="8" height="8" viewBox="0 0 8 8"><path d="M1 4l2 2 4-5" stroke="#c4161c" stroke-width="1.5" fill="none"/></svg>Design-Build</li>
        <li><svg width="8" height="8" viewBox="0 0 8 8"><path d="M1 4l2 2 4-5" stroke="#c4161c" stroke-width="1.5" fill="none"/></svg>Interior Renovation</li>
      </ul>
    </div>
  </div>
</section>

</body>
</html>
```